automatic Real Estate Sales Brochure

Print-out of 3 to 8 pages automatically on a color inkjet printer. Page size A4
All details for my Real Estate Sales Design Project are in attached file.
Here some points:
We have abound 100 real estate objects for sale (houses, flats and pieces of land).
For each item, our system creates automatically a sales documentation, which we print out and hand to the potential buyers after they've visited the object or send it by mail upon request in form of a pdf.
This document should be of 3 to maximum 8 pages.
It should be of a modern design and invite the client to read it.
The information should be clear and quick to find.
If the global look could somehow relate to the look of our web site www.norvelhaus.ch, that would be nice.
The company data is there for legal reasons, but it is the agent's phone and mail that the clients should use for contact.
The photos should be of big size (2 by page?) without being distorted nor cut.
Optionally, to save ink and pages, maybe only the first 3-4 photos full size and the rest smaller?

Target Market(s)

will be printed or sent as PDF "on the fly", meaning no pre-printing at a print shop!

Industry/Entity Type

Real Estate

Font styles to use
Sans Serif

Requirements
Must have
• see details in attached file
Should not have
• no edge-to-edge printing
• no double-page printing (A3)

```html
<!DOCTYPE html>
<html lang="fr">
<head>
<meta charset="utf-8">
<title>Brochure de vente immobilière</title>
<link href="https://fonts.googleapis.com/css2?family=Oswald:wght@400;500;600&family=Roboto:wght@400;700&display=swap" rel="stylesheet">
<style>
:root{
  --bg:#3b302a;
  --paper:#ececec;
  --red:#e0101a;
  --ink:#2a2a2a;
  --grey:#555;
  --band:#3a3a3a;
  --frame:#111;
}
*{margin:0;padding:0;box-sizing:border-box}
html,body{width:1200px;height:1200px;overflow:hidden;background:var(--bg)}
body{position:relative;font-family:Roboto,Arial,sans-serif;color:var(--ink)}
.page{position:absolute;width:279px;height:372px;background:var(--paper);overflow:hidden}
.p1{left:17px;top:183px}.p2{left:309px;top:183px}.p3{left:604px;top:183px}.p4{left:899px;top:183px}
.p5{left:17px;top:643px}.p6{left:309px;top:643px}.p7{left:604px;top:643px}.p8{left:899px;top:643px}
.abs{position:absolute}
.brand{position:absolute;font-family:Oswald,sans-serif;font-weight:600;color:var(--red);letter-spacing:.5px;line-height:1}
.brand-center{left:0;right:0;text-align:center;font-size:13px}
.photo{position:absolute;border:2px solid var(--frame)}
.ph-top{left:41px;top:33px;width:196px;height:146px}
.ph-bottom{left:40px;top:186px;width:199px;height:148px}
.balcony{background:linear-gradient(160deg,#8fb8dc 0%,#c9d7c0 35%,#b69a7a 70%,#d8c3a0 100%)}
.garden{background:linear-gradient(170deg,#a8c7e3 0%,#5e8f3c 40%,#3f6a2a 100%)}
.house{background:linear-gradient(170deg,#9fc0df 0%,#a35a4a 45%,#c0385a 75%,#4c6a30 100%)}
.facade{background:linear-gradient(120deg,#4e5d35 0%,#d8d2c4 45%,#8a5a40 100%)}
.room{background:linear-gradient(180deg,#ebe6dc 0%,#e0d8c8 55%,#b77a3a 70%,#9a5e26 100%)}
.wardrobe{background:linear-gradient(90deg,#f0e6c8 0%,#e6d6a8 40%,#2a2a2a 45%,#3a3a3a 100%)}
.bath{background:linear-gradient(180deg,#e8e8e8 0%,#d6d6d6 60%,#bdbdbd 100%)}
.kitchen{background:linear-gradient(180deg,#eeeae2 0%,#e6dcc8 55%,#c49a62 75%,#a87a40 100%)}
.footer{position:absolute;left:0;right:0;top:343px;height:14px;background:var(--band);color:#ddd;font-size:3.6px;line-height:4px;display:flex;align-items:center;justify-content:space-between;padding:0 22px}
.footer .item{display:flex;align-items:center;gap:3px}
.dot{display:inline-block;width:4px;height:4px;border-radius:50%;background:var(--red);flex:none}
/* cover */
.cover-brand{left:0;right:0;text-align:center;top:30px;font-size:20px}
.tagline{left:0;right:0;text-align:center;top:68px;font-family:Oswald,sans-serif;font-size:10.5px;line-height:14px;color:#333}
.tag-rule{left:89px;width:101px;top:86px;height:1px;background:var(--red)}
.cover-photo{left:21px;top:107px;width:236px;height:154px}
.cover-kicker{left:0;right:0;text-align:center;top:277px;font-family:Oswald,sans-serif;font-weight:500;font-size:16px;line-height:18px;color:var(--red);letter-spacing:.3px}
.cover-title{left:0;right:0;text-align:center;top:298px;font-family:Oswald,sans-serif;font-weight:600;font-size:29px;line-height:32px;color:#222}
.cover-url{left:0;right:0;text-align:center;top:347px;font-size:5px;letter-spacing:.6px;color:#333}
/* page 2 */
.head-brand{left:19px;top:13px;font-size:13px}
.addr{left:19px;top:30px;font-size:5px;font-weight:700;line-height:8.5px;color:#222}
.contact{left:19px;top:49px;font-size:5px;line-height:8px;color:#222}
.contact li{list-style:none;display:flex;align-items:center;gap:3px}
.contact .name{color:var(--red);font-style:italic;font-weight:700}
.head-rule{left:19px;width:215px;top:75px;height:2px;background:#222}
.agent{left:199px;top:12px;width:67px;height:67px;border-radius:50%;border:2px solid #222;background:radial-gradient(circle at 50% 40%,#c8a48a 0%,#6a4a3a 60%,#3a2a24 100%)}
.sec{position:absolute;font-size:5.6px;line-height:7px;font-weight:700;color:var(--red);border-bottom:.6px solid var(--red);padding-bottom:.5px}
.body-text{position:absolute;font-size:4.3px;line-height:5.3px;color:#333}
.body-text p{margin-bottom:4px}
.small-ph{position:absolute;border:1px solid var(--frame)}
/* page 3 */
.specs{left:19px;top:99px;width:246px;border:1px solid #333;border-radius:4px;overflow:hidden;font-size:4px}
.specs table{width:100%;border-collapse:collapse}
.specs td{padding:3.5px 3px;color:#333;border-right:.6px solid #999;white-space:nowrap}
.specs td:last-child{border-right:0}
.specs tr:nth-child(odd){background:#e4e4e4}
.specs tr:nth-child(even){background:#9a9a9a;height:4px}
.specs tr:nth-child(even) td{padding:0}
.specs .k{color:var(--red);font-weight:700}
.feat{left:19px;top:172px;width:246px;height:66px;border:1px solid #333;border-radius:4px;display:flex;padding:5px 6px;font-size:4px;color:#333}
.feat ul{list-style:none;flex:1}
.feat ul+ul{border-left:.6px solid #333;padding-left:8px}
.feat li{height:11.8px;display:flex;align-items:center;gap:3px;white-space:nowrap}
.feat .k{color:var(--red);font-weight:700}
.tick{width:4px;height:4px;flex:none}
</style>
</head>
<body>

<section class="page p1">
  <div class="brand cover-brand">norvelhaus</div>
  <div class="abs tagline">Spécialiste Romand De Vente Immobilière</div>
  <div class="abs tag-rule"></div>
  <div class="photo cover-photo balcony" role="img" aria-label="Photo du balcon avec vue sur le parc"></div>
  <div class="abs cover-kicker">LUMINEUX 4.5 DE 100M2</div>
  <div class="abs cover-title">IDÉALEMENT SITUÉ</div>
  <div class="abs cover-url">www.norvelhaus.ch</div>
</section>

<section class="page p2">
  <div class="brand head-brand">norvelhaus</div>
  <div class="abs addr">Lumineux 4.5 de 100m2 Idéalement Situé<br>Chemin des Aulnes ,1200 Genève</div>
  <ul class="abs contact">
    <li><span class="dot"></span><span class="name">Mira Castell</span></li>
    <li><span class="dot"></span>castell@norvelhaus.ch</li>
    <li><span class="dot"></span>077 000 11 22</li>
  </ul>
  <div class="abs head-rule"></div>
  <div class="abs agent" role="img" aria-label="Portrait de la courtière"></div>
  <div class="sec" style="left:19px;top:87px">DESCRIPTION</div>
  <div class="body-text" style="left:19px;top:100px;width:240px">
    <p>Venez visiter sans tarder ce bel appartement situé dans un environnement calme et vert, proche du centre-ville et des commodités. Il profite de beaux volumes et de pièces très lumineuses.</p>
    <p>Cet appartement conviendra aussi pour un investissement locatif.</p>
    <p>Il est en bon état d'entretien et attend ses nouveaux propriétaires !</p>
    <p>Il se distribue ainsi :</p>
    <p>Une entrée avec armoire encastrée dessert la partie jour et la partie nuit. La cuisine ouverte est entièrement équipée. Le séjour donne accès à un agréable balcon avec vue dégagée sur le parc.</p>
    <p>La partie nuit offre trois belles chambres, une salle de bains avec baignoire et un wc visiteurs.</p>
    <p>Deux places de parc intérieures s'ajoutent à ce bel appartement !</p>
    <p>N'hésitez pas à me contacter pour plus d'informations et une visite !</p>
  </div>
  <div class="small-ph garden" style="left:20px;top:249px;width:116px;height:84px" role="img" aria-label="Photo du jardin de la résidence"></div>
  <div class="small-ph balcony" style="left:150px;top:249px;width:116px;height:84px" role="img" aria-label="Photo du balcon"></div>
  <footer class="footer">
    <span class="item"><span class="dot"></span><span>Norvelhaus Sàrl,<br>1899 Mervelin</span></span>
    <span class="item"><span class="dot"></span>021 000 40 50</span>
    <span class="item"><span class="dot"></span>www.norvelhaus.ch</span>
  </footer>
</section>

<section class="page p3">
  <div class="brand brand-center" style="top:20px">norvelhaus</div>
  <div class="sec" style="left:19px;top:48px">SITUATION</div>
  <div class="body-text" style="left:19px;top:60px;width:246px">Cet appartement a l'avantage d'être proche de toutes les commodités, à 3 minutes du collège, à 1 minute de l'arrêt de bus et à 3 minutes des axes autoroutiers. Centre-ville en 7 minutes.</div>
  <div class="sec" style="left:19px;top:88px">APPARTEMENT, MAISON, TERRAIN</div>
  <div class="abs specs">
    <table>
      <tr><td><span class="k">CHF</span> ------------910'000</td><td><span class="k">SURFACE HABITABLE</span> -- 100m2</td><td><span class="k">SURFACE PARCELLE</span> -- 1'000m2</td></tr>
      <tr><td></td><td></td><td></td></tr>
      <tr><td><span class="k">PIÈCES</span> ------------4.5</td><td><span class="k">ANNÉE</span> ----------------1994</td><td style="text-align:center;color:var(--red)">–</td></tr>
      <tr><td></td><td></td><td></td></tr>
      <tr><td><span class="k">DISPONIBLE</span> ----- 1.1.2018</td><td><span class="k">ETAT</span> ------------------BON ÉTAT</td><td style="text-align:center;color:var(--red)">–</td></tr>
      <tr><td></td><td></td><td></td></tr>
    </table>
  </div>
  <div class="sec" style="left:19px;top:160px">CARACTÉRISTIQUES</div>
  <div class="abs feat">
    <ul>
      <li><svg class="tick" viewBox="0 0 10 10"><circle cx="5" cy="5" r="4" fill="none" stroke="#333" stroke-width="1.2"/><path d="M3 5l1.5 1.5L7 3.5" fill="none" stroke="#333" stroke-width="1.2"/></svg><span class="k">ETAGE</span> : 1er étage</li>
      <li><svg class="tick" viewBox="0 0 10 10"><circle cx="5" cy="5" r="4" fill="none" stroke="#333" stroke-width="1.2"/><path d="M3 5l1.5 1.5L7 3.5" fill="none" stroke="#333" stroke-width="1.2"/></svg><span class="k">VUE</span> : Vue dégagée sur le parc</li>
      <li><svg class="tick" viewBox="0 0 10 10"><circle cx="5" cy="5" r="4" fill="none" stroke="#333" stroke-width="1.2"/><path d="M3 5l1.5 1.5L7 3.5" fill="none" stroke="#333" stroke-width="1.2"/></svg><span class="k">COMMERCES</span> : à proximité immédiate</li>
      <li><svg class="tick" viewBox="0 0 10 10"><circle cx="5" cy="5" r="4" fill="none" stroke="#333" stroke-width="1.2"/><path d="M3 5l1.5 1.5L7 3.5" fill="none" stroke="#333" stroke-width="1.2"/></svg><span class="k">ECOLES</span> : Collège des Tilleuls</li>
      <li><svg class="tick" viewBox="0 0 10 10"><circle cx="5" cy="5" r="4" fill="none" stroke="#333" stroke-width="1.2"/><path d="M3 5l1.5 1.5L7 3.5" fill="none" stroke="#333" stroke-width="1.2"/></svg><span class="k">TRANSPORT PUBLIC</span> : à 5 minutes à pied</li>
    </ul>
    <ul>
      <li><svg class="tick" viewBox="0 0 10 10"><circle cx="5" cy="5" r="4" fill="none" stroke="#333" stroke-width="1.2"/><path d="M3 5l1.5 1.5L7 3.5" fill="none" stroke="#333" stroke-width="1.2"/></svg><span class="k">CHAUFFAGE</span> : Mazout / au sol</li>
      <li><svg class="tick" viewBox="0 0 10 10"><circle cx="5" cy="5" r="4" fill="none" stroke="#333" stroke-width="1.2"/><path d="M3 5l1.5 1.5L7 3.5" fill="none" stroke="#333" stroke-width="1.2"/></svg><span class="k">CAVE</span> : Oui</li>
      <li><svg class="tick" viewBox="0 0 10 10"><circle cx="5" cy="5" r="4" fill="none" stroke="#333" stroke-width="1.2"/><path d="M3 5l1.5 1.5L7 3.5" fill="none" stroke="#333" stroke-width="1.2"/></svg><span class="k">GARAGE</span> : 2 places de parc intérieures</li>
      <li><svg class="tick" viewBox="0 0 10 10"><circle cx="5" cy="5" r="4" fill="none" stroke="#333" stroke-width="1.2"/><path d="M3 5l1.5 1.5L7 3.5" fill="none" stroke="#333" stroke-width="1.2"/></svg><span class="k">BALCON</span> : Oui</li>
      <li><svg class="tick" viewBox="0 0 10 10"><circle cx="5" cy="5" r="4" fill="none" stroke="#333" stroke-width="1.2"/><path d="M3 5l1.5 1.5L7 3.5" fill="none" stroke="#333" stroke-width="1.2"/></svg><span class="k">ASCENSEUR</span> : Oui</li>
    </ul>
  </div>
  <div class="small-ph house" style="left:22px;top:250px;width:113px;height:84px" role="img" aria-label="Photo d'une maison voisine et de massifs fleuris"></div>
  <div class="small-ph facade" style="left:148px;top:250px;width:113px;height:84px" role="img" aria-label="Photo de la façade de l'immeuble"></div>
  <footer class="footer">
    <span class="item"><span class="dot"></span><span>Norvelhaus Sàrl,<br>1899 Mervelin</span></span>
    <span class="item"><span class="dot"></span>021 000 40 50</span>
    <span class="item"><span class="dot"></span>www.norvelhaus.ch</span>
  </footer>
</section>

<section class="page p4">
  <div class="brand brand-center" style="top:14px">norvelhaus</div>
  <div class="photo ph-top room" role="img" aria-label="Photo du couloir d'entrée"></div>
  <div class="photo ph-bottom wardrobe" role="img" aria-label="Photo d'une chambre avec armoire encastrée"></div>
  <footer class="footer">
    <span class="item"><span class="dot"></span><span>Norvelhaus Sàrl,<br>1899 Mervelin</span></span>
    <span class="item"><span class="dot"></span>021 000 40 50</span>
    <span class="item"><span class="dot"></span>www.norvelhaus.ch</span>
  </footer>
</section>

<section class="page p5">
  <div class="brand brand-center" style="top:14px">norvelhaus</div>
  <div class="photo ph-top bath" role="img" aria-label="Photo de la salle de bains"></div>
  <div class="photo ph-bottom room" role="img" aria-label="Photo d'une chambre lumineuse"></div>
  <footer class="footer">
    <span class="item"><span class="dot"></span><span>Norvelhaus Sàrl,<br>1899 Mervelin</span></span>
    <span class="item"><span class="dot"></span>021 000 40 50</span>
    <span class="item"><span class="dot"></span>www.norvelhaus.ch</span>
  </footer>
</section>

<section class="page p6">
  <div class="brand brand-center" style="top:17px">norvelhaus</div>
  <div class="photo ph-top room" role="img" aria-label="Photo du séjour avec baies vitrées"></div>
  <div class="photo ph-bottom kitchen" role="img" aria-label="Photo du séjour ouvert sur la cuisine"></div>
  <footer class="footer">
    <span class="item"><span class="dot"></span><span>Norvelhaus Sàrl,<br>1899 Mervelin</span></span>
    <span class="item"><span class="dot"></span>021 000 40 50</span>
    <span class="item"><span class="dot"></span>www.norvelhaus.ch</span>
  </footer>
</section>

<section class="page p7">
  <div class="brand brand-center" style="top:17px">norvelhaus</div>
  <div class="photo ph-top kitchen" role="img" aria-label="Photo de la cuisine ouverte"></div>
  <div class="photo ph-bottom bath" role="img" aria-label="Photo de la cuisine et des armoires du hall"></div>
  <footer class="footer">
    <span class="item"><span class="dot"></span><span>Norvelhaus Sàrl,<br>1899 Mervelin</span></span>
    <span class="item"><span class="dot"></span>021 000 40 50</span>
    <span class="item"><span class="dot"></span>www.norvelhaus.ch</span>
  </footer>
</section>

<section class="page p8">
  <div class="brand brand-center" style="top:15px">norvelhaus</div>
  <div class="photo ph-top balcony" role="img" aria-label="Photo du balcon avec vue sur le parc"></div>
  <div class="photo ph-bottom kitchen" role="img" aria-label="Photo de la cuisine avec îlot"></div>
  <footer class="footer">
    <span class="item"><span class="dot"></span><span>Norvelhaus Sàrl,<br>1899 Mervelin</span></span>
    <span class="item"><span class="dot"></span>021 000 40 50</span>
    <span class="item"><span class="dot"></span>www.norvelhaus.ch</span>
  </footer>
</section>

</body>
</html>
```